Providing Back Office Solutions to Financial Advisors and Attorney Needs a Business Card Design

Need a Business Card Design that speaks to Financial Advisor and Attorneys. Some of the word that come to mind is Clean/Simple & Futuristic.

Industry/Entity Type

Business

```html
<!DOCTYPE html>
<html lang="en">
<head>
<meta charset="utf-8">
<title>Veridan Business Card</title>
<link href="https://fonts.googleapis.com/css2?family=Roboto:wght@400;500;700&display=swap" rel="stylesheet">
<style>
:root{
  --page:#3a3532;
  --card:#161616;
  --brand:#1c7fd4;
  --brand-soft:#2a63b8;
  --title:#6a63c9;
  --ink:#f2f2f2;
  --rule:#8a8a8a;
}
*{margin:0;padding:0;box-sizing:border-box}
html,body{width:1200px;height:780px;overflow:hidden}
body{background:var(--page);font-family:'Roboto',Arial,sans-serif;position:relative}
.card{position:absolute;width:540px;height:309px;background:var(--card);border-radius:18px;box-shadow:0 12px 30px rgba(0,0,0,.45)}
.card-front{left:40px;top:236px}
.card-back{left:620px;top:236px}
.brand{position:absolute;display:flex;align-items:center}
.brand-square{width:46px;height:46px;background:var(--brand);margin-right:14px}
.brand-divider{width:1px;height:66px;background:var(--brand-soft);margin-right:14px}
.brand-name{font-weight:500;font-size:40px;letter-spacing:3px;color:var(--brand);line-height:1}
.brand-tagline{font-weight:400;font-size:12.5px;letter-spacing:.8px;color:var(--brand-soft);margin-top:6px}
.card-front .brand{left:34px;top:118px}
.card-back .brand{left:124px;top:118px}
.front-divider{position:absolute;left:316px;top:96px;width:1px;height:118px;background:var(--rule)}
.contact{position:absolute;left:336px;top:96px;color:var(--ink)}
.contact-name{font-weight:700;font-size:19px}
.contact-role{font-size:13px;color:var(--title);margin-bottom:8px}
.contact-line{display:flex;align-items:center;font-size:13px;line-height:20px}
.contact-line svg{width:13px;height:13px;margin-right:10px;flex:none}
</style>
</head>
<body>
<section class="card card-front">
  <div class="brand">
    <div class="brand-square"></div>
    <div class="brand-divider"></div>
    <div>
      <div class="brand-name">VERIDAN</div>
      <div class="brand-tagline">BACK OFFICE SOLUTIONS</div>
    </div>
  </div>
  <div class="front-divider"></div>
  <div class="contact">
    <div class="contact-name">Daniel Hart</div>
    <div class="contact-role">Managing Director</div>
    <div class="contact-line">
      <svg viewBox="0 0 14 14"><circle cx="7" cy="7" r="7" fill="#1c7fd4"/><path d="M4.5 3.8c.4-.3.8-.2 1 .2l.6 1.1c.2.4 0 .7-.3.9-.3.2-.2.5 0 .8.5.8 1 1.3 1.8 1.8.3.2.6.2.8 0 .2-.3.5-.5.9-.3l1.1.6c.4.2.5.6.2 1-.9 1.1-2.4.8-4-.6-1.6-1.5-2.9-3.9-2.1-5.5z" fill="#161616"/></svg>
      555-014 0200
    </div>
    <div class="contact-line">
      <svg viewBox="0 0 14 14"><circle cx="7" cy="7" r="7" fill="#1c7fd4"/><rect x="4.8" y="3" width="4.4" height="8" rx=".8" fill="#161616"/><rect x="5.6" y="4" width="2.8" height="5" fill="#1c7fd4"/></svg>
      555-018-4417
    </div>
    <div class="contact-line">
      <svg viewBox="0 0 14 14"><circle cx="7" cy="7" r="7" fill="#1c7fd4"/><rect x="3.5" y="6" width="7" height="4.5" rx=".6" fill="#161616"/><rect x="5" y="3.5" width="4" height="2.8" fill="#161616"/></svg>
      555-027 3381
    </div>
    <div class="contact-line">
      <svg viewBox="0 0 14 14"><circle cx="7" cy="7" r="7" fill="#1c7fd4"/><rect x="3.5" y="4.5" width="7" height="5" rx=".5" fill="#161616"/><path d="M3.8 4.8 7 7.4l3.2-2.6" stroke="#1c7fd4" stroke-width=".8" fill="none"/></svg>
      dan@veridanbo.com
    </div>
  </div>
</section>

<section class="card card-back">
  <div class="brand">
    <div class="brand-square"></div>
    <div class="brand-divider"></div>
    <div>
      <div class="brand-name">VERIDAN</div>
      <div class="brand-tagline">BACK OFFICE SOLUTIONS</div>
    </div>
  </div>
</section>
</body>
</html>
```